business card/stationary design
business card/stationary
Use same font as used in my logo
Use different font if you think it looks better
Professional
Glen R. Whitmore
Managing Partner
4197-B West Harlow Creek Rd.
Alder Springs, OR 97411
glen.whitmore@bluelanternfinancialgroup.example
Bluelanternfinancialgroup.example
I want a clean professional looking card and simple stationary design.
nothing

```html
<!DOCTYPE html>
<html lang="en">
<head>
<meta charset="utf-8">
<title>Blue Lantern Financial Group – Business Card</title>
<link rel="stylesheet" href="https://fonts.googleapis.com/css2?family=Cinzel:wght@400;700&family=Tinos:wght@400;700&display=swap">
<style>
  :root {
    --backdrop: #e9e6e2;
    --card-white: #ffffff;
    --maroon: #7a1a2c;
    --maroon-dark: #5c1020;
    --maroon-muted: #8a2236;
    --gold: #c9a04a;
    --gold-light: #e2c27a;
    --ink: #4a4a4a;
    --card-dark: #2a2222;
    --card-dark-2: #3a2e2c;
    --website-dark: #8a7a6e;
  }
  * { box-sizing: border-box; margin: 0; padding: 0; }
  html, body { width: 1200px; height: 996px; overflow: hidden; }
  body {
    background: var(--backdrop);
    position: relative;
    font-family: "Tinos", "Times New Roman", serif;
  }
  .card {
    position: absolute;
    width: 670px;
    height: 385px;
    border-radius: 26px;
    overflow: hidden;
    box-shadow: 0 6px 18px rgba(0,0,0,0.25);
  }
  /* Front */
  .card-front { left: 129px; top: 94px; background: var(--card-white); }
  .name-band {
    position: absolute; left: 0; right: 0; top: 40px; height: 72px;
    background: linear-gradient(180deg, var(--maroon) 0%, var(--maroon-dark) 100%);
    border-top: 3px solid var(--gold);
    border-bottom: 3px solid var(--gold);
    display: flex; align-items: center; justify-content: center;
    color: #fff; font-size: 22px;
  }
  .name-band .person { color: var(--gold-light); font-weight: 700; }
  .name-band .sep { margin: 0 8px; color: #fff; }
  .gold-rule {
    position: absolute; left: 0; right: 0; top: 122px; height: 2px; background: var(--gold);
  }
  .brand {
    position: absolute; left: 0; right: 0; top: 168px;
    text-align: center; font-family: "Cinzel", "Times New Roman", serif;
    font-weight: 700; color: var(--maroon);
  }
  .brand .brand-line1 { font-size: 44px; letter-spacing: 2px; display: flex; align-items: center; justify-content: center; gap: 14px; }
  .brand .brand-mark { width: 22px; height: 22px; border-radius: 50%; background: var(--maroon); display: inline-block; }
  .brand .brand-line2 { font-size: 26px; letter-spacing: 2px; margin-top: 2px; }
  .contact {
    position: absolute; left: 0; right: 0; top: 292px;
    color: var(--ink); font-size: 14px;
  }
  .contact-row { display: flex; justify-content: center; align-items: center; gap: 8px; margin-bottom: 9px; }
  .contact-row .item { display: inline-flex; align-items: center; gap: 7px; }
  .contact-row .item + .item { margin-left: 22px; }
  .icon { width: 14px; height: 14px; fill: var(--gold); flex: none; }
  /* Back */
  .card-back { left: 404px; top: 517px; background: var(--card-dark); }
  .back-texture {
    position: absolute; inset: 0;
    background: radial-gradient(circle at 30% 35%, var(--card-dark-2) 0%, var(--card-dark) 70%);
  }
  .back-brand {
    position: absolute; left: 0; right: 0; top: 140px; text-align: center;
    font-family: "Cinzel", "Times New Roman", serif; font-weight: 700; color: var(--maroon-muted);
  }
  .back-brand .brand-line1 { font-size: 40px; letter-spacing: 2px; display: flex; align-items: center; justify-content: center; gap: 12px; }
  .back-brand .brand-mark { width: 20px; height: 20px; border-radius: 50%; background: var(--maroon-muted); display: inline-block; }
  .back-brand .brand-line2 { font-size: 24px; letter-spacing: 2px; }
  .back-web {
    position: absolute; left: 0; right: 0; top: 298px;
    display: flex; justify-content: center; align-items: center; gap: 8px;
    color: var(--website-dark); font-size: 14px;
  }
</style>
</head>
<body>

<section class="card card-front">
  <div class="name-band">
    <span class="person">Glen R. Whitmore</span><span class="sep">|</span><span class="role">Managing Partner</span>
  </div>
  <div class="gold-rule"></div>

  <div class="brand">
    <div class="brand-line1"><span class="brand-mark"></span>Blue Lantern</div>
    <div class="brand-line2">Financial Group</div>
  </div>

  <div class="contact">
    <div class="contact-row">
      <span class="item">
        <svg class="icon" viewBox="0 0 16 16"><path d="M8 1 1 7h2v8h4v-5h2v5h4V7h2z"/></svg>
        4197-B West Harlow Creek Rd. Alder Springs, OR 97411
      </span>
    </div>
    <div class="contact-row">
      <span class="item">
        <svg class="icon" viewBox="0 0 16 16"><path d="M4 1 6 5 4.5 6.5a9 9 0 0 0 5 5L11 10l4 2-1 3C7 15 1 9 1 2z"/></svg>
        541-555-0142
      </span>
      <span class="item">
        <svg class="icon" viewBox="0 0 16 16"><rect x="3" y="1" width="10" height="5"/><rect x="1" y="6" width="14" height="6" rx="1"/><rect x="4" y="10" width="8" height="5"/></svg>
        541-555-0187
      </span>
    </div>
    <div class="contact-row">
      <span class="item">
        <svg class="icon" viewBox="0 0 16 16"><path d="M1 3h14v10H1zM1 3l7 6 7-6" fill="none" stroke="#c9a04a" stroke-width="1.5"/></svg>
        glen.whitmore@bluelanternfinancialgroup.example
      </span>
      <span class="item">
        <svg class="icon" viewBox="0 0 16 16"><circle cx="8" cy="8" r="7"/></svg>
        Bluelanternfinancialgroup.example
      </span>
    </div>
  </div>
</section>

<section class="card card-back">
  <div class="back-texture" role="img" aria-label="Soft dark brown background with faint scattered light circles"></div>
  <div class="back-brand">
    <div class="brand-line1"><span class="brand-mark"></span>Blue Lantern</div>
    <div class="brand-line2">Financial Group</div>
  </div>
  <div class="back-web">
    <svg class="icon" viewBox="0 0 16 16"><circle cx="8" cy="8" r="7"/></svg>
    Bluelanternfinancialgroup.example
  </div>
</section>

</body>
</html>
```